R7M Horizon Business Card Design

We need a business card created for our New Business "R7M Horizon"<br/><br/>The business card design is up to you however the following information must be on the business card:<br/><br/>Front of the business card -<br/>Email :tobyw@r7mhorizon.nz<br/>Mobile: +64 (0) 22 4871 569<br/>Website: www.r7mhorizon.nz<br/>Card Owner Name: Tobias Wrenhall<br/>Company Title: Business Development Manager<br/>Slogan: "The BEST of both worlds". <br/>Logo On the front attached to the design brief<br/><br/>On the back: <br/>Space on the back for 4 more versions of the logo across the bottom of the card indicating different subsidiary brands - R7M Coffee, R7M Arts, R7M ?? (The card will be used for all of these brands - We Will add the extra subsidiary logos to the design once the design is finished (We are a graphics design team). <br/><br/>Other than that we want a premium feeling logo that remains universally usable depending on the business entity that we are using the card for. The use of bright bold colours would be great but we still want the card to feel premium.
Target Market(s)
Gift Design and Manufacturing Companies
Contact Information for Business Card
Front of the business card -
Email :tobyw@r7mhorizon.nz
Mobile: +64 (0) 22 4871 569
Website: www.r7mhorizon.nz
Card Owner Name: Tobias Wrenhall
Company Title: Business Development Manager
Slogan: "The BEST of both worlds".
Logo On the front attached to the design brief

```html
<!DOCTYPE html>
<html lang="en">
<head>
<meta charset="utf-8">
<title>R7M Horizon Business Card</title>
<link rel="stylesheet" href="https://fonts.googleapis.com/css2?family=Poppins:ital,wght@0,400;0,500;0,600;0,700;1,500&display=swap">
<style>
  :root {
    --brand-blue: #3a48a6;
    --brand-blue-light: #5261b9;
    --ink-dark: #2b2b30;
    --ink-mid: #45454d;
    --card-white: #ffffff;
    --stage: #e9e7e3;
    --texture-grey: rgba(214, 216, 224, 0.55);
    --texture-white: rgba(255, 255, 255, 0.12);
  }
  * { box-sizing: border-box; margin: 0; padding: 0; }
  html, body {
    width: 900px; height: 1200px; overflow: hidden;
    background: var(--stage);
    font-family: "Poppins", sans-serif;
  }
  .canvas { position: relative; width: 900px; height: 1200px; }

  .card {
    position: absolute; left: 82px; width: 733px; height: 428px;
    border-radius: 28px; overflow: hidden;
    box-shadow: 0 6px 14px rgba(0,0,0,0.25);
  }
  .card--front { top: 137px; background: var(--card-white); }
  .card--back {
    top: 633px;
    background: radial-gradient(circle at 50% 35%, var(--brand-blue-light) 0%, var(--brand-blue) 60%);
  }

  /* soft tonal area standing in for the dotted sphere texture */
  .sphere-texture { position: absolute; }
  .card--front .sphere-texture {
    left: 400px; top: -20px; width: 360px; height: 420px;
    background: radial-gradient(closest-side at 60% 50%, var(--texture-grey) 0%, rgba(214,216,224,0.25) 55%, rgba(214,216,224,0) 100%);
  }
  .card--back .sphere-texture {
    left: 400px; top: -10px; width: 360px; height: 420px;
    background: radial-gradient(closest-side at 60% 50%, var(--texture-white) 0%, rgba(255,255,255,0.06) 55%, rgba(255,255,255,0) 100%);
  }

  .wordmark {
    position: absolute; font-weight: 700; white-space: nowrap; letter-spacing: 0.3px;
  }
  .card--front .wordmark {
    left: 83px; top: 183px; font-size: 34px; line-height: 52px; color: var(--brand-blue);
  }
  .card--back .wordmark {
    left: 0; right: 0; text-align: center; top: 180px;
    font-size: 44px; line-height: 66px; color: #fff;
  }

  .divider {
    position: absolute; left: 344px; top: 141px; width: 2px; height: 148px;
    background: var(--brand-blue);
  }

  .owner { position: absolute; left: 366px; top: 137px; }
  .owner__name { font-size: 22px; color: var(--brand-blue); line-height: 30px; text-transform: uppercase; }
  .owner__name strong { font-weight: 700; }
  .owner__name span { font-weight: 400; }
  .owner__title { font-size: 15px; font-weight: 500; color: var(--ink-mid); line-height: 26px; }

  .contacts { position: absolute; left: 366px; top: 204px; list-style: none; }
  .contacts li {
    display: flex; align-items: center; gap: 10px;
    font-size: 15.5px; color: var(--ink-dark); height: 28px;
  }
  .contacts svg { width: 18px; height: 18px; flex: none; }

  .tagline {
    position: absolute; left: 0; right: 0; top: 383px; text-align: center;
    font-size: 14px; font-style: italic; font-weight: 500; color: var(--brand-blue);
  }

  .sub-brands {
    position: absolute; left: 163px; top: 360px; width: 407px;
    display: flex; justify-content: space-between; list-style: none;
  }
  .sub-brands li {
    color: #fff; font-size: 15px; font-weight: 700; white-space: nowrap; line-height: 24px;
  }
</style>
</head>
<body>
<main class="canvas">
  <section class="card card--front" aria-label="Card front">
    <div class="sphere-texture" role="img" aria-label="Faint halftone dotted sphere decoration"></div>
    <div class="wordmark">R7M Horizon</div>
    <div class="divider"></div>
    <div class="owner">
      <p class="owner__name"><strong>Tobias</strong> <span>Wrenhall</span></p>
      <p class="owner__title">Business Development Manager</p>
    </div>
    <ul class="contacts">
      <li>
        <svg viewBox="0 0 18 18"><circle cx="9" cy="9" r="8.2" fill="none" stroke="#3a48a6" stroke-width="1.4"/><path d="M6.2 5.2l1.4-.3.8 1.9-.9.7c.5 1 1.2 1.7 2.2 2.2l.7-.9 1.9.8-.3 1.4c-3 .2-6-2.8-5.8-5.8z" fill="#3a48a6"/></svg>
        +64 (0) 22 4871 569
      </li>
      <li>
        <svg viewBox="0 0 18 18"><circle cx="9" cy="9" r="8.2" fill="none" stroke="#3a48a6" stroke-width="1.4"/><rect x="5" y="6" width="8" height="6" fill="#3a48a6"/><path d="M5 6l4 3.2L13 6" fill="none" stroke="#fff" stroke-width="0.9"/></svg>
        tobyw@r7mhorizon.nz
      </li>
      <li>
        <svg viewBox="0 0 18 18"><circle cx="9" cy="9" r="8.2" fill="none" stroke="#3a48a6" stroke-width="1.4"/><circle cx="9" cy="9" r="4.5" fill="none" stroke="#3a48a6" stroke-width="1"/><ellipse cx="9" cy="9" rx="2" ry="4.5" fill="none" stroke="#3a48a6" stroke-width="1"/><path d="M4.5 9h9" stroke="#3a48a6" stroke-width="1"/></svg>
        www.r7mhorizon.nz
      </li>
    </ul>
    <p class="tagline">The BEST of both worlds</p>
  </section>

  <section class="card card--back" aria-label="Card back">
    <div class="sphere-texture" role="img" aria-label="Faint halftone dotted sphere decoration"></div>
    <div class="wordmark">R7M Horizon</div>
    <ul class="sub-brands">
      <li>R7M Coffee</li>
      <li>R7M Arts</li>
      <li>R7M Graphic</li>
      <li>R7M Apps</li>
    </ul>
  </section>
</main>
</body>
</html>
```